Revamp Of Landing Page For an Automated AI Voice Agents Agency

here is my current landing page https://app.brightfernpromoworks.biz/v2/preview/KXWPLmA4rHdQZyNvBtEJ?notrack=true

Please use all my current content and imagery of ai agents in your new design. Make it easy to ready, easy to navigate and easy to understand

I am looking for a SLEEK shiny polished looking website. I like Dark themed sites but am open to see light themed sites too so please dont be shy.

The site should have an Ai Voice Agent Theme about it. Maybe look and feel of futureistic but simple and not intimidating to the average person...

Here are a couple website designs I like for reference:
https://q4w.io/
https://ai-bots.morentavelik.com/
https://chatquarry.com/ai-agents

Target Market(s)

b2b

Industry/Entity Type

AI Voice Agents

Coding

Font styles to use
Other font styles liked:
• open

Requirements
Must have
• all elements and content and images used in existing design.
Nice to have
• open
Should not have
• open

```html
<!DOCTYPE html>
<html lang="en">
<head>
<meta charset="utf-8">
<title>Voxora – AI Voice Agents</title>
<link rel="stylesheet" href="https://fonts.googleapis.com/css2?family=Poppins:ital,wght@0,400;0,500;0,600;0,700;1,400;1,500&display=swap">
<style>
:root{
  --bg:#0a0d22;
  --bg-deep:#070918;
  --panel:#0c1029;
  --violet:#5a4fe6;
  --plum:#8e40c8;
  --line:#8b6cff;
  --yellow:#fff200;
  --ink:#ffffff;
  --muted:#c9c8e6;
  --teal:#4fd6e6;
}
*{box-sizing:border-box;margin:0;padding:0}
html,body{width:1200px;height:4405px;overflow:hidden}
body{
  position:relative;font-family:"Poppins",sans-serif;color:var(--ink);
  background:
    radial-gradient(ellipse 600px 700px at 1150px 200px, rgba(120,60,200,.55), transparent 70%),
    radial-gradient(ellipse 500px 500px at 80px 500px, rgba(70,50,170,.35), transparent 70%),
    radial-gradient(ellipse 700px 500px at 100px 2950px, rgba(60,50,180,.35), transparent 70%),
    linear-gradient(180deg,#241a55 0,#151235 500px,var(--bg) 1000px,var(--bg) 4405px);
}
.abs{position:absolute}
.center{left:0;width:1200px;text-align:center}
.logo{display:flex;align-items:center;gap:10px;font-weight:600;letter-spacing:3px;color:var(--ink)}
.logo-dot{width:22px;height:22px;border:2px solid var(--ink);border-radius:50%}
.btn{display:flex;align-items:center;justify-content:center;background:var(--yellow);color:#111;
  font-weight:700;font-size:12px;letter-spacing:.4px;border-radius:22px;text-transform:uppercase}
.note{font-style:italic;font-size:11px;line-height:15px;color:var(--muted)}
.hero-title{font-size:40px;font-weight:600;line-height:45px}
.section-title{font-size:37px;font-weight:600}
.hero-media{left:121px;top:542px;width:956px;height:425px;border:2px solid var(--line);
  background:radial-gradient(ellipse 260px 330px at 50% 60%,#c9d9e6,#5a6fa0 45%,transparent 70%),
  linear-gradient(90deg,#0b1450,#101a6a 30%,#1b1450 70%,#3a1a6a);}
.card{position:absolute;width:306px;height:235px;border:2px solid var(--line);overflow:hidden}
.card-photo{background:linear-gradient(160deg,#9fb4c8 0%,#4a5f7a 35%,#1a2438 75%,#0d1322 100%)}
.card-body{position:absolute;left:18px;right:18px;bottom:16px}
.card h3{font-size:18px;font-weight:500;margin-bottom:4px}
.card .tag{color:var(--yellow);font-size:10px;font-weight:600;line-height:12px}
.card p{font-size:9.5px;line-height:12px;color:#e6e6f2}
.card-feature{left:446px;top:1107px;width:306px;height:483px;text-align:center;
  background:linear-gradient(180deg,var(--violet),var(--plum));border:none}
.portrait{position:absolute;left:45px;top:34px;width:215px;height:215px;border-radius:50%;
  border:4px solid #0b0f24;background:radial-gradient(circle at 50% 40%,#d8dde6,#6b7a9a 55%,#1a2a55)}
.box{border:2px solid var(--line)}
.feature{position:absolute;top:2240px;width:318px;height:140px;padding-left:92px}
.feature h4{font-size:15px;font-weight:500;margin-top:80px}
.feature p{font-size:11px;line-height:14px;color:var(--muted);margin-top:4px}
.divider{position:absolute;top:2228px;width:1px;height:150px;background:rgba(255,255,255,.2)}
.promo{background:linear-gradient(135deg,var(--violet),var(--plum));border:1px solid var(--line)}
.promise-card{width:306px;height:177px;border:2px solid var(--line);text-align:center;padding-top:20px}
.promise-card h4{font-size:14px;font-weight:600;margin-top:12px}
.promise-card p{font-size:11px;line-height:14px;color:var(--muted);margin-top:4px}
.faq{left:121px;width:956px;border:2px solid var(--line);display:flex;justify-content:space-between;
  padding:0 26px;font-size:15px;font-weight:500}
.faq.open{background:linear-gradient(90deg,var(--violet),var(--plum));flex-direction:column;justify-content:center}
.faq small{font-size:10px;font-weight:400;margin-top:6px}
.footer-text{font-size:10px;line-height:16px;text-align:center;color:#e8e8f2}
</style>
</head>
<body>

<!-- Header -->
<div class="abs logo" style="left:121px;top:24px;font-size:22px"><span>VOXORA</span><span class="logo-dot"></span></div>
<div class="abs btn" style="left:937px;top:20px;width:140px;height:35px">Get Started</div>

<!-- Hero -->
<h1 class="abs center hero-title" style="top:110px">Ai Voice Agents That Answer Calls,<br>Book Appts, Send Emails, Text<br>Messages, Follow Up Reminders,<br>Transfer Calls &amp; More For You 24<br>Hours 7 Days A Week!</h1>
<div class="abs btn" style="left:477px;top:366px;width:246px;height:34px">Get An Instant Free Demo</div>
<p class="abs center note" style="top:424px">We Will Create An Ai Agent Customized For Your Business At No Cost. Simply Click The Button Above And Your Very Own Ai<br>Agent Will Be Calling You In Just A Couple Minutes. Experience The Magic And Get Ready To Be Very Impressed!</p>
<div class="abs hero-media" role="img" aria-label="AI receptionist with headset in front of glowing blue and purple sound waves"></div>

<!-- Workforce -->
<h2 class="abs center section-title" style="top:1018px">Meet Your New AI-Powered Workforce</h2>

<div class="card card-photo" style="left:121px;top:1107px" role="img" aria-label="AI sales agent wearing a headset in a city office">
  <div class="card-body"><h3>Ai Sales Agent</h3>
  <p>Deron will take your inbound sales calls. Will give all detailed information to the customer, answer questions in a normal conversational tone and can book sales appointments or transfer hot prospects to a human to close the sale.</p></div>
</div>
<div class="card card-photo" style="left:771px;top:1107px" role="img" aria-label="AI follow up agent with headset at a desk">
  <div class="card-body"><h3>Ai Follow Up Reminders</h3>
  <div class="tag">Calls, Sends SMS &amp; Email Reminders</div>
  <p>Tovin handles all the follow up calls, appt reminders and sends out the email and sms reminders too.</p></div>
</div>
<div class="card card-photo" style="left:121px;top:1355px" role="img" aria-label="AI appointment setter with headset in an office">
  <div class="card-body"><h3>Ai Appointment Setter</h3>
  <div class="tag">Book Appts &amp; Reservations On Auto Pilot</div>
  <p>Marek offers business advice, helps brainstorm ideas, and provides insights on growth tactics to support your entrepreneurial journey.</p></div>
</div>
<div class="card card-photo" style="left:771px;top:1355px" role="img" aria-label="AI lead qualifier with headset in a night office">
  <div class="card-body"><h3>Ai Lead Qualifier</h3>
  <div class="tag">Conversate With Prospects To Qualify<br>Before Handing Over To Sales Team</div>
  <p>All of our ai agents gather information and qualify leads.</p></div>
</div>
<div class="card card-feature">
  <div class="portrait" role="img" aria-label="Portrait of the AI receptionist"></div>
  <h3 class="abs" style="left:0;width:100%;top:270px">Ai Receptionist</h3>
  <p class="abs" style="left:20px;right:20px;top:305px;font-size:11px;line-height:15px;font-weight:500">Takes Overflow and After Hours Calls or Can<br>Take Calls 24/7 &amp; Transfer To Appropriate Dept.</p>
  <p class="abs" style="left:20px;right:20px;top:352px;font-size:10px;line-height:14px">Jalen handles all your calls 24/7. You can also set him to only take overflow calls and after hours. He can send emails and sms messages and even book appointments over the call</p>
  <div class="abs btn" style="left:30px;top:424px;width:246px;height:34px">Get An Instant Free Demo</div>
</div>
<p class="abs center note" style="top:1625px">We Will Create An Ai Agent Customized For Your Business At No Cost. Simply Click The Button Above And Your Very Own Ai<br>Agent Will Be Calling You In Just A Couple Minutes. Experience The Magic And Get Ready To Be Very Impressed!</p>

<!-- Wish -->
<p class="abs" style="left:121px;top:1733px;font-size:18px;font-weight:500">Install the power of AI for your business</p>
<h2 class="abs" style="left:121px;top:1766px;font-size:38px;font-weight:600;line-height:45px">Your wish Is their<br>command</h2>
<p class="abs" style="left:121px;top:1874px;font-size:11px;font-weight:600;color:var(--yellow)">Your New Ai Agents Will Never Call In Sick And Will Never Complain!</p>
<p class="abs" style="left:121px;top:1910px;width:440px;font-size:11.5px;line-height:18px">With your new team of AI Agents, handling inbound calls, sending emails and sms messages, booking appointments and handling customer service inquiries is going to save you a ton of time and money.</p>
<div class="abs btn" style="left:121px;top:2001px;width:248px;height:35px">Get An Instant Free Demo</div>
<div class="abs" role="img" aria-label="Friendly robot with headphones beside a glowing chat bubble" style="left:615px;top:1692px;width:462px;height:402px;background:radial-gradient(ellipse 180px 200px at 60% 45%,#5fd8e8 0%,#2a6a8a 35%,#18204a 65%,transparent 80%)"></div>

<!-- Never sick -->
<div class="abs box" style="left:121px;top:2102px;width:956px;height:325px;background:var(--bg-deep)"></div>
<h2 class="abs center section-title" style="top:2146px">An Employee that Never Gets Sick!</h2>
<svg class="abs" style="left:215px;top:2230px" width="58" height="60" viewBox="0 0 58 60" fill="none" stroke="#8b6cff" stroke-width="2"><path d="M20 56v-10h-8l2-10-6-4 6-6c0-14 10-22 22-22 12 0 18 10 18 20 0 8-6 14-8 18v14"/><circle cx="32" cy="22" r="8"/><path d="M32 10v4M32 30v4M20 22h4M40 22h4"/></svg>
<svg class="abs" style="left:508px;top:2230px" width="62" height="60" viewBox="0 0 62 60" fill="none" stroke="#8b6cff" stroke-width="2"><circle cx="31" cy="30" r="26"/><ellipse cx="31" cy="30" rx="11" ry="26"/><path d="M5 30h52M9 16h44M9 44h44"/></svg>
<svg class="abs" style="left:832px;top:2230px" width="66" height="62" viewBox="0 0 66 62" fill="none" stroke="#8b6cff" stroke-width="2"><circle cx="16" cy="16" r="12"/><circle cx="50" cy="46" r="12"/><circle cx="50" cy="12" r="7"/><circle cx="16" cy="50" r="7"/><path d="M28 16h15M23 50h15"/></svg>
<div class="feature" style="left:121px"><h4>Trained In Seconds</h4><p>Learns Your Entire Website<br>In Seconds</p></div>
<div class="divider" style="left:441px"></div>
<div class="feature" style="left:417px"><h4>Worldwide</h4><p>Works Anywhere In The Globe</p></div>
<div class="divider" style="left:759px"></div>
<div class="feature" style="left:741px"><h4>User-friendly</h4><p>Your AI Agents Sound As If<br>They're Real Humans</p></div>

<!-- Hire -->
<div class="abs promo" style="left:121px;top:2437px;width:956px;height:362px"></div>
<h2 class="abs center section-title" style="top:2482px">Our Ai Agents Our Ready To Be Hired</h2>
<p class="abs center" style="top:2542px;font-size:15px;font-weight:500">Lightning-Fast Responses</p>
<p class="abs center" style="top:2571px;font-size:15px;font-weight:500">Instant answers, no coffee, bathroom or lunch breaks needed</p>
<div class="abs btn" style="left:477px;top:2640px;width:246px;height:35px">Get An Instant Free Demo</div>
<p class="abs center note" style="top:2712px;color:#eee">We Will Create An Ai Agent Customized For Your Business At No Cost. Simply Click The Button Above And Your Very Own Ai<br>Agent Will Be Calling You In Just A Couple Minutes. Experience The Magic And Get Ready To Be Very Impressed!</p>

<!-- Promise -->
<div class="abs" role="img" aria-label="Glowing microphone icon with pink and blue voice waveform" style="left:0;top:2837px;width:410px;height:419px;background:radial-gradient(circle at 170px 210px,#e04ad8 0,#6a3ad0 14%,#2a2a8a 32%,#14164a 55%,transparent 72%)"></div>
<h2 class="abs section-title" style="left:446px;top:2885px">Our Promise To You:</h2>
<div class="abs promise-card" style="left:446px;top:2957px">
  <svg width="60" height="60" viewBox="0 0 60 60" fill="none" stroke="#8b6cff" stroke-width="2"><circle cx="30" cy="30" r="26"/><circle cx="30" cy="30" r="18"/><path d="M36 23c-2-3-12-3-12 2s12 3 12 9-10 5-12 2M30 17v26"/></svg>
  <h4 style="margin-top:18px">14-day money-back guarantee*</h4>
</div>
<div class="abs promise-card" style="left:771px;top:2957px">
  <svg width="60" height="60" viewBox="0 0 60 60" fill="none" stroke="#8b6cff" stroke-width="2"><circle cx="30" cy="24" r="10"/><path d="M14 26a16 16 0 0 1 32 0M12 48c4-10 12-12 18-12s14 2 18 12H12z"/><rect x="10" y="24" width="6" height="10" rx="2"/><rect x="44" y="24" width="6" height="10" rx="2"/></svg>
  <h4>24/7 Customer Support</h4>
  <p>Often praised for our friendly<br>&amp; helpful support team</p>
</div>
<p class="abs" style="left:446px;top:3162px;font-size:18px;font-weight:500;line-height:25px">After Our Customers Have A Conversation With Their New<br>Ai Voice Agent They Give Us 5 Stars!</p>
<svg class="abs" style="left:446px;top:3232px" width="140" height="26" viewBox="0 0 140 26" fill="#fff200">
  <g id="star"><polygon points="13,1 16.5,9 25,9.5 18.5,15 20.5,24 13,19.5 5.5,24 7.5,15 1,9.5 9.5,9"/></g>
  <use href="#star" x="28"/><use href="#star" x="56"/><use href="#star" x="84"/><use href="#star" x="112"/>
</svg>

<!-- FAQ -->
<h2 class="abs center section-title" style="top:3332px">An Employee that Never Gets Sick!</h2>
<div class="abs faq" style="top:3409px;height:52px;align-items:center"><span>What exactly are the AI Voice Agents?</span><span>+</span></div>
<div class="abs faq open" style="top:3478px;height:73px">
  <div style="display:flex;justify-content:space-between"><span>How will these AI Voice Agents benefit</span><span>–</span></div>
  <small>Ai Voice Agents Answer Calls, Book Appts, Send Emails, Text Messages, Follow Up Reminders &amp; More For You 24/7!</small>
</div>
<div class="abs faq" style="top:3567px;height:53px;align-items:center"><span>Are they easy to use?</span><span>+</span></div>

<!-- CTA -->
<div class="abs promo" style="left:121px;top:3656px;width:956px;height:362px"></div>
<h2 class="abs center" style="top:3703px;font-size:40px;font-weight:600;line-height:45px">These AI Agents Can Help<br>Your Business Tremendously.<br>Imagine The Possibilities</h2>
<div class="abs btn" style="left:477px;top:3859px;width:246px;height:35px">Get An Instant Free Demo</div>
<p class="abs center note" style="top:3931px;color:#eee">We Will Create An Ai Agent Customized For Your Business At No Cost. Simply Click The Button Above And Your Very Own Ai<br>Agent Will Be Calling You In Just A Couple Minutes. Experience The Magic And Get Ready To Be Very Impressed!</p>

<!-- Footer -->
<div class="abs logo" style="left:121px;top:4072px;font-size:28px"><span>VOXORA</span><span class="logo-dot" style="width:28px;height:28px"></span></div>
<p class="abs" style="left:390px;top:4078px;font-size:19px;font-weight:500">Newsletter Signup</p>
<div class="abs" style="left:586px;top:4071px;width:359px;height:41px;border:1px solid #555a7a;border-radius:4px;background:var(--bg-deep);font-size:11px;padding:13px 12px">Email</div>
<div class="abs" style="left:959px;top:4071px;width:118px;height:41px;border-radius:4px;background:var(--violet);font-size:12px;font-weight:500;display:flex;align-items:center;justify-content:center">Subscribe</div>
<div class="abs" style="left:121px;top:4163px;width:956px;height:1px;background:rgba(255,255,255,.25)"></div>
<div class="abs center footer-text" style="top:4188px">
  © 2025 Voxora AI<br>
  *14-Day Money Back Guarantee Terms: If you use the ai agents and you're not happy. Then you can contact us in the first 14 days for a full refund.<br>
  <span style="display:block;margin-top:4px">DISCLAIMER:</span>
  <span style="display:block;margin-top:8px">PRIVACY | TERMS &amp; CONDITIONS | EARNINGS &amp; PRODUCTS DISCLAIMER</span>
  <span style="display:block;margin-top:6px">Do you have questions about ( ) Please email ( )</span>
  <span style="display:block;margin-top:6px">IMPORTANT: This site is not a part of the Linkverse website or Linkverse Inc. Additionally, this site is NOT endorsed by Linkverse in any way.</span>
  <span style="display:block;margin-top:6px">LINKVERSE is a trademark of LINKVERSE, Inc.</span>
</div>

</body>
</html>
```